HVL Regal Business Card Design 2020

Harbor Vale Living is looking for a business card that is clean and straight to the point but still looks high-end and attractive. We are a team comprised of management and field professionals focused on the high-end residential marketplace. We serve homeowners and trade professionals directly based out of the Metrowest/Boston area. We provide client services as well as construction/renovation services.
We are aiming for a black and white feel (white background and black text) and a matte finish with rounded edges.

We want to emphasis our vision of "Properties - Projects - Partners".
Dana Pritchell is the president of HVL

Please include the following areas we service: Boston/Cape/Newport
Please make sure to include Dana's mobile (617) 555 0143 & office number (617) 555 0187, email dana@harborvaleliving.example and website www.harborvaleliving.example

Colors

Designer to choose only greyscale colors for use in the design.

Requirements
Must have
• Include "Properties - Projects - Partners" in design

Include "After Hours Emergency Support # 1800 555 0199" with icon

```html
<!DOCTYPE html>
<html lang="en">
<head>
<meta charset="utf-8">
<title>Harbor Vale Living — Business Card</title>
<link rel="stylesheet" href="https://fonts.googleapis.com/css2?family=Raleway:wght@700&family=Roboto:wght@400;500&family=Montserrat:wght@600&display=swap">
<style>
  :root {
    --backdrop: #d8d8d8;
    --card-light: #ffffff;
    --card-dark: #2a2a2a;
    --ink: #232323;
    --ink-soft: #3a3a3a;
    --brand-grey: #9a9a9a;
    --on-dark: #f2f2f2;
  }
  * { box-sizing: border-box; margin: 0; padding: 0; }
  html, body { width: 1173px; height: 1200px; overflow: hidden; }
  body { background: var(--backdrop); position: relative; font-family: "Roboto", sans-serif; }

  .card { position: absolute; left: 205px; width: 742px; height: 410px; }
  .card--front { top: 150px; background: var(--card-light); }
  .card--back { top: 637px; background: var(--card-dark); }

  .name-marker { position: absolute; left: 0; top: 63px; width: 22px; height: 46px; background: var(--ink); }
  .identity { position: absolute; left: 60px; top: 60px; }
  .identity__name { font-family: "Raleway", sans-serif; font-weight: 700; font-size: 27px; color: var(--ink); letter-spacing: 0.2px; line-height: 1.1; }
  .identity__title { font-weight: 500; font-size: 20px; color: var(--ink-soft); line-height: 1.3; }

  .contacts { position: absolute; left: 60px; top: 250px; list-style: none; }
  .contacts li { display: flex; align-items: center; height: 25px; font-size: 19.5px; color: var(--ink-soft); white-space: nowrap; }
  .contacts svg { width: 18px; height: 18px; margin-right: 7px; fill: var(--ink); flex: none; }

  .emergency { position: absolute; left: 60px; top: 362px; display: flex; align-items: center; font-size: 15px; font-weight: 500; color: var(--ink); white-space: nowrap; }
  .emergency svg { width: 18px; height: 18px; margin-right: 7px; fill: var(--ink); flex: none; }

  .brand { position: absolute; display: flex; align-items: center; font-family: "Montserrat", sans-serif; font-weight: 600; white-space: nowrap; }
  .brand--front { right: 60px; top: 300px; color: var(--ink); font-size: 20px; gap: 10px; }
  .brand--front .brand__mark { width: 14px; height: 14px; background: var(--ink); }
  .brand--back { left: 0; right: 0; top: 160px; justify-content: center; color: var(--brand-grey); font-size: 34px; letter-spacing: 2px; gap: 16px; }
  .brand--back .brand__mark { width: 22px; height: 22px; background: var(--brand-grey); }

  .tagline { position: absolute; left: 0; right: 0; top: 236px; text-align: center; font-family: "Montserrat", sans-serif; font-weight: 600; font-size: 15px; letter-spacing: 3px; color: var(--brand-grey); text-transform: uppercase; }

  .areas { position: absolute; left: 0; right: 0; top: 358px; text-align: center; color: var(--on-dark); font-size: 19.5px; white-space: nowrap; }
  .areas span::before { content: "\25CF"; font-size: 13px; margin: 0 6px 0 8px; vertical-align: 2px; }
</style>
</head>
<body>
  <section class="card card--front">
    <div class="name-marker"></div>
    <div class="identity">
      <h1 class="identity__name">DANA PRITCHELL</h1>
      <p class="identity__title">President</p>
    </div>
    <ul class="contacts">
      <li><svg viewBox="0 0 18 18"><path d="M5 1h8a1.5 1.5 0 0 1 1.5 1.5v13A1.5 1.5 0 0 1 13 17H5a1.5 1.5 0 0 1-1.5-1.5v-13A1.5 1.5 0 0 1 5 1zm0 2v11h8V3zm4 12.2a.8.8 0 1 0 0-.01z"/></svg>(617) 555 0143</li>
      <li><svg viewBox="0 0 18 18"><path d="M1 6c2-3 14-3 16 0l-1 2h-3l-.5-2h-7L5 8H2zm3 3h10l2 7H2zm5 1.5a2.5 2.5 0 1 0 0 5 2.5 2.5 0 0 0 0-5z"/></svg>(617) 555 0187</li>
      <li><svg viewBox="0 0 18 18"><path d="M1 4h16v11H1zm1.5 1.5v.4L9 10.5l6.5-4.6v-.4zm0 2.2v5.8l4-3zm13 0l-4 2.8 4 3zM7.8 11.2l-4.6 2.3h11.6l-4.6-2.3L9 12z"/></svg>dana@harborvaleliving.example</li>
      <li><svg viewBox="0 0 18 18"><path d="M9 1a8 8 0 1 0 0 16A8 8 0 0 0 9 1zm-2 3c1 .5 2 1.5 1.5 2.5S6 7 6 8.5 8 11 7.5 13 5 14 4 13c-1-2-1-5 0-7 .8-1.2 2-2.3 3-2zm5 1c1.5 1 2.5 3 2 5-.5 1-1.5 0-2-1s-1.5-1-1.5-2 .5-2 1.5-2z"/></svg>www.harborvaleliving.example</li>
    </ul>
    <p class="emergency"><svg viewBox="0 0 18 18"><path d="M9 1L17 16H1zm-1 5v5h2V6zm0 6.5v2h2v-2z"/></svg>After Hours Emergency Support # 1800 555 0199</p>
    <div class="brand brand--front"><span class="brand__mark"></span>Harbor Vale Living</div>
  </section>

  <section class="card card--back">
    <div class="brand brand--back"><span class="brand__mark"></span>Harbor Vale Living</div>
    <p class="tagline">Properties - Projects - Partners</p>
    <p class="areas"><span>Boston</span><span>Metrowest</span><span>South Shore</span><span>Cape</span><span>Newport</span></p>
  </section>
</body>
</html>
```